/ custom plush toys for luxury hotel /

We are, a US company that makes custom plush toys for luxury hotels only. (our customers)
our logo is a mascot:
a teddy bear dressing up as a hotel concierge, the message is: in terms of teddy bear we are your concierge
These plushies are intended to be offered to the children of the customers of these luxurious hotels.
To convince our customers who will land on this site to contact us and work with us, we want to convey the message that our client (the hotel) will make HIS client and HIS children happy by offering them an unexpected gift at the check-in , also to make understand that it is very powerful advertising and marketing object for the hotel (this plush and its LOGO obviously will accompany the children of these customers everywhere).
We also want to insist on the fact that our solution is turnkey, starting from your wishes we take care of everything from the creation of the design to the delivery of the finished products, you do not worry about anything else.
Here is our process:
We only do custom, the customer gives us his theme and ideas and from that we propose different designs, drawing, 3D visualizations, once the design is approved, we make a physical sample that we have validated or modified by our client...
We would like to have a website/landing page to present our concept and our company, also to involve our future customers to contact us by mail or phone, this should be the objective of this page
We want to use themes like teddy bear, luxury, , kids, custom made, handmade, hand drawing..
We really want to emphasize the customization: we create your teddy bear from scratch.
We do not have a catalog because made-to-measure and therefore really want to involve our future customers to contact us by mail.
I can provide you with some of this content (sources file available):
Our Logo
Pictures of some plushies that we made this year
Drawings,
3D
a brief comic strip that we made to present us
Here are some examples attached .
also: Some content that I don't have but that I think would fit in the thematic:
happy children with a teddy bear /
the steps of manufacturing (a seamstress? / the selection of a fabric?) / a designer at work on a drawing board /
etc
Waiting for your proposal,
available if precisions needed
Thank you for your time
Tobi
Luxury Hotel Manager / Purchaser

```html
<!DOCTYPE html>
<html lang="en">
<head>
<meta charset="utf-8">
<title>Velvet Porter – Custom Plush Toys for Luxury Hotels</title>
<link href="https://fonts.googleapis.com/css2?family=Poppins:wght@300;400;500;600&family=Varela+Round&display=swap" rel="stylesheet">
<style>
:root{
  --purple:#4b4a97;
  --navy:#0e0c26;
  --ink:#2b2a6b;
  --orange:#f18563;
  --rust:#c96d4a;
  --salmon:#f08a6f;
  --yellow:#f5bf2c;
  --gold:#f5c342;
  --grey:#e9e9ec;
  --white:#ffffff;
  --muted:#8d8da6;
  --head:"Varela Round",sans-serif;
  --body:"Poppins",sans-serif;
}
*{box-sizing:border-box;margin:0;padding:0}
html,body{width:1200px;height:5344px;overflow:hidden}
body{position:relative;background:var(--grey);font-family:var(--body);color:var(--ink)}
.abs{position:absolute}
.bg{position:absolute;left:0;top:0}
.nav{left:0;top:66px;width:1200px;display:flex;justify-content:center;gap:36px;font-size:12px;color:#fff}
.nav a{color:#fff;text-decoration:none}
.nav a.active{color:var(--orange)}
.nav-icons{right:62px;top:66px;display:flex;gap:18px}
.photo{border-radius:0}
.hero-art{left:135px;top:135px;width:375px;height:615px;border-radius:45% 45% 30% 30%;background:linear-gradient(160deg,#a8582f 0%,#7a3f22 35%,#2f2d78 60%,#23225c 100%)}
.hero-title{left:637px;top:312px;font-family:var(--head);font-size:27px;line-height:35px;color:var(--orange);letter-spacing:.3px}
.hero-text{left:637px;top:398px;width:410px;font-size:11.5px;line-height:18px;color:#fff}
.btn{display:inline-block;background:var(--orange);color:#fff;border-radius:20px;font-size:12px;font-weight:500;text-align:center}
.hero-btn{left:637px;top:460px;width:132px;height:35px;line-height:35px}
.section-title{font-family:var(--head);font-size:26px;color:var(--ink);text-align:center;width:1200px;left:0;letter-spacing:.5px}
.lead{left:0;width:1200px;text-align:center;font-size:12px;color:var(--muted)}
.bubble{width:228px;height:178px;border-radius:50%;display:flex;flex-direction:column;align-items:center;justify-content:center;text-align:center;color:#fff}
.bubble h3{font-family:var(--head);font-weight:400;font-size:17px;line-height:21px}
.bubble p{font-size:10.5px;line-height:13px;margin-top:4px;opacity:.9}
.child-photo{left:446px;top:1121px;width:291px;height:498px;background:linear-gradient(180deg,#e9e9ec 0%,#d9b79a 30%,#c99a78 60%,#a9a3c6 100%);border-radius:140px 140px 0 0}
.step{width:300px}
.step .num{font-family:var(--head);font-size:44px;color:var(--ink);line-height:52px;border-bottom:2px solid var(--ink);padding-bottom:4px}
.step h3{font-family:var(--head);font-weight:400;font-size:22px;margin-top:14px;color:var(--ink)}
.step p{font-size:12.5px;line-height:19px;color:var(--muted);margin-top:12px}
.step hr{border:0;border-top:2px solid #d4d4de;margin-top:24px}
.work-head{left:180px;top:2385px;width:295px;text-align:right;color:#fff}
.work-head h2{font-family:var(--head);font-weight:400;font-size:27px}
.work-head p{font-size:12.5px;line-height:19px;margin-top:14px}
.work-item{left:588px;width:420px;display:flex;gap:34px}
.work-item .ico{flex:0 0 62px;height:62px;border-radius:50%;background:#fff;display:flex;align-items:center;justify-content:center}
.work-item h3{font-family:var(--head);font-weight:400;font-size:24px;color:var(--gold)}
.work-item p{font-size:12.5px;line-height:20px;color:#fff;margin-top:4px}
.gallery-main{left:77px;top:3274px;width:660px;height:457px;background:radial-gradient(ellipse at 50% 55%,#e8b27a 0%,#f3e6d8 40%,#f5f5f5 70%)}
.thumb{top:3768px;height:214px;background:radial-gradient(ellipse at 50% 55%,#e3ac78 0%,#efe3d6 45%,#f4f4f4 75%)}
.gallery-head{left:783px;top:3440px;width:280px}
.gallery-head h2{font-family:var(--head);font-weight:400;font-size:27px;color:var(--ink)}
.gallery-head p{font-size:12px;line-height:19px;color:var(--muted);margin-top:14px}
.say-head{left:77px;top:4126px;width:200px}
.say-head h2{font-family:var(--head);font-weight:400;font-size:27px;line-height:34px;color:var(--ink)}
.say-head p{font-size:12px;line-height:19px;color:var(--muted);margin-top:14px}
.card{top:4106px;height:218px;background:#fff;padding:76px 32px 0}
.card p{font-size:12px;line-height:19px;color:var(--muted)}
.card h4{font-family:var(--head);font-weight:400;font-size:15px;color:var(--ink);margin-top:22px}
.card small{display:block;font-size:10px;color:var(--muted)}
.card .quote{position:absolute;right:36px;bottom:10px;font-family:Georgia,serif;font-size:72px;line-height:72px;color:var(--ink);font-weight:700}
.avatar{width:82px;height:82px;border-radius:50%;position:absolute;top:-44px;left:32px;border:4px solid #fff}
.scallop{left:0;top:4400px;width:1200px;height:14px;background:radial-gradient(circle at 50% 100%,var(--navy) 9px,transparent 10px) 0 0/25px 14px repeat-x}
.contact{left:77px;top:4522px;width:1044px;height:456px;border-radius:8px;overflow:hidden;display:flex}
.contact .intro{width:521px;background:var(--purple);color:#fff;padding:150px 0 0 131px}
.contact .intro h2{font-family:var(--head);font-weight:400;font-size:25px;line-height:34px}
.contact .intro p{font-size:12px;line-height:19px;margin-top:16px;width:270px}
.contact form{flex:1;background:#fff;padding:44px 52px 0 52px}
.field{border-bottom:1.5px solid #c9c9d4;height:40px;margin-bottom:24px;font-size:11.5px;color:#b3b3c2;padding-top:4px}
.send{margin:22px 0 0 218px;width:88px;height:32px;line-height:32px}
.footer{top:5065px;color:#fff}
.footer h4{font-family:var(--head);font-weight:400;font-size:14px}
.footer li{list-style:none;font-size:10px;line-height:23px;opacity:.85}
.footer .contact-line{display:flex;gap:8px;align-items:flex-start;font-size:9.5px;line-height:13px;margin-top:8px;opacity:.9}
.footer-col{text-align:center;width:120px}
.legal{left:270px;top:5212px;width:660px;border-top:1px solid rgba(255,255,255,.5);padding-top:10px;font-size:8.5px;color:#fff;opacity:.85}
.social{right:270px;top:5220px;display:flex;gap:16px}
.social span{width:12px;height:12px;border-radius:50%;background:#fff;display:block}
</style>
</head>
<body>

<svg class="bg" width="1200" height="5344" viewBox="0 0 1200 5344" aria-hidden="true">
  <rect width="1200" height="5344" fill="var(--grey)"/>
  <path d="M0 0H1200V640C1050 690 900 700 760 740 600 770 300 720 0 716Z" fill="#f4f4f6"/>
  <path d="M0 0H1200V480C1060 455 960 500 840 590 720 690 580 640 430 590 300 548 160 610 0 580Z" fill="var(--purple)"/>
  <ellipse cx="872" cy="698" rx="146" ry="92" fill="var(--purple)"/>
  <path d="M0 1660C300 1630 650 1640 900 1652 1060 1658 1140 1648 1200 1640V2230C900 2250 300 2250 0 2210Z" fill="#f4f4f6"/>
  <rect x="0" y="2200" width="1200" height="1298" fill="#fff"/>
  <path d="M0 2210C300 2250 900 2250 1200 2200V3190C960 3205 730 3240 665 3080 600 2910 320 2750 0 2775Z" fill="var(--navy)"/>
  <rect x="0" y="4412" width="1200" height="932" fill="var(--navy)"/>
</svg>

<nav class="abs nav">
  <a class="active" href="#">Home</a><a href="#">About Us</a><a href="#">Why Us</a><a href="#">Our Process</a><a href="#">Work with Us</a><a href="#">Our Gallery</a><a href="#">What People Say</a>
</nav>
<div class="abs nav-icons">
  <svg width="16" height="16" viewBox="0 0 16 16" fill="none" stroke="#f18563" stroke-width="1.6"><circle cx="7" cy="7" r="5"/><path d="M11 11l4 4"/></svg>
  <svg width="14" height="16" viewBox="0 0 14 16" fill="none" stroke="#f18563" stroke-width="1.6"><circle cx="7" cy="5" r="3.5"/><path d="M1 15c0-4 3-6 6-6s6 2 6 6"/></svg>
</div>

<div class="abs hero-art" role="img" aria-label="Mascot illustration: teddy bear dressed as a hotel concierge, waving"></div>
<h1 class="abs hero-title">Excepteur sint occaecat<br>cupidatat non proident</h1>
<p class="abs hero-text">Ut enim ad minim veniam, quis nostrud exercitation ullamco laboris nisi ut aliquip ex ea commodo consequat.</p>
<a class="abs btn hero-btn" href="#">Contact Us</a>

<h2 class="abs section-title" style="top:878px">WHO WE ARE</h2>
<p class="abs lead" style="top:930px">We are a Velvet Porter , a US company that makes custom plush toys for luxury hotels only.</p>

<h2 class="abs section-title" style="top:1032px">WHY PLUSH TOYS ARE AMAZING?</h2>
<div class="abs bubble" style="left:187px;top:1138px;background:var(--rust)"><h3>They Give<br>Great Hugs</h3><p>Excepteur sint occaecat<br>cupidatat non proident</p></div>
<div class="abs bubble" style="left:187px;top:1360px;background:var(--purple)"><h3>Children Will<br>Love Them</h3><p>Excepteur sint occaecat<br>cupidatat non proident</p></div>
<div class="abs bubble" style="left:772px;top:1138px;background:var(--salmon)"><h3>They Don't Break</h3><p>Excepteur sint occaecat<br>cupidatat non proident</p></div>
<div class="abs bubble" style="left:772px;top:1360px;background:var(--yellow)"><h3>They Have<br>Cute Shape</h3><p>Excepteur sint occaecat<br>cupidatat non proident</p></div>
<div class="abs child-photo" role="img" aria-label="Photo: smiling young girl hugging a teddy bear"></div>

<h2 class="abs section-title" style="top:1705px">HERE IS OUR PROCESS</h2>
<div class="abs step" style="left:77px;top:1800px"><div class="num">01</div><h3>Explore Idea</h3><p>Duis aute irure dolor in reprehenderit in voluptate velit esse cillum dolore eu fugiat nulla pariatur.</p><p>Excepteur sint occaecat cupidatat non proident, sunt in culpa qui officia deserunt mollit anim id est laborum.</p><hr><p>Duis aute irure dolor in reprehenderit in voluptate velit esse cillum dolore eu fugiat nulla pariatur.</p></div>
<div class="abs step" style="left:450px;top:1800px"><div class="num">02</div><h3>Design Process</h3><p>Duis aute irure dolor in reprehenderit in voluptate velit esse cillum dolore eu fugiat nulla pariatur.</p><p>Excepteur sint occaecat cupidatat non proident, sunt in culpa qui officia deserunt mollit anim id est laborum.</p><hr><p>Duis aute irure dolor in reprehenderit in voluptate velit esse cillum dolore eu fugiat nulla pariatur.</p></div>
<div class="abs step" style="left:824px;top:1800px"><div class="num">03</div><h3>3D Visualizations</h3><p>Duis aute irure dolor in reprehenderit in voluptate velit esse cillum dolore eu fugiat nulla pariatur.</p><p>Excepteur sint occaecat cupidatat non proident, sunt in culpa qui officia deserunt mollit anim id est laborum.</p><hr><p>Duis aute irure dolor in reprehenderit in voluptate velit esse cillum dolore eu fugiat nulla pariatur.</p></div>
<svg class="abs" style="left:1156px;top:1962px" width="14" height="24" viewBox="0 0 14 24" fill="none" stroke="var(--ink)" stroke-width="2"><path d="M2 2l10 10-10 10"/></svg>

<div class="abs work-head"><h2>WORK WITH US</h2><p>Excepteur sint occaecat cupidatat non proident, sunt in culpa qui officia deserunt mollit anim id est laborum.</p></div>
<div class="abs work-item" style="top:2370px">
  <div class="ico"><svg width="30" height="24" viewBox="0 0 30 24" fill="none" stroke="var(--orange)" stroke-width="1.8"><rect x="2" y="2" width="26" height="20" rx="2"/><path d="M2 4l13 10 13-10"/></svg></div>
  <div><h3>Contact Us</h3><p>Duis aute irure dolor in reprehenderit in voluptate velit esse cillum dolore eu fugiat nulla pariatur. Excepteur sint occaecat cupidatat non proident, sunt in culpa qui officia deserunt mollit anim id est laborum.</p></div>
</div>
<div class="abs work-item" style="top:2578px">
  <div class="ico"><svg width="30" height="28" viewBox="0 0 30 28" fill="none" stroke="var(--orange)" stroke-width="1.8"><path d="M3 3h16v11H10l-5 4v-4H3z"/><path d="M22 10h5v11h-2v4l-5-4h-8v-4"/></svg></div>
  <div><h3>Explain What You Want</h3><p>Duis aute irure dolor in reprehenderit in voluptate velit esse cillum dolore eu fugiat nulla pariatur. Excepteur sint occaecat cupidatat non proident, sunt in culpa qui officia deserunt mollit anim id est laborum.</p></div>
</div>
<div class="abs work-item" style="top:2785px">
  <div class="ico"><svg width="30" height="28" viewBox="0 0 30 28" fill="none" stroke="var(--orange)" stroke-width="1.8"><rect x="2" y="2" width="26" height="18" rx="1"/><path d="M11 26h8M15 20v6M7 15l5-6 4 4 6-7"/></svg></div>
  <div><h3>Design Process</h3><p>Duis aute irure dolor in reprehenderit in voluptate velit esse cillum dolore eu fugiat nulla pariatur. Excepteur sint occaecat cupidatat non proident, sunt in culpa qui officia deserunt mollit anim id est laborum.</p></div>
</div>
<div class="abs work-item" style="top:2993px">
  <div class="ico"><svg width="30" height="28" viewBox="0 0 30 28" fill="none" stroke="var(--orange)" stroke-width="1.8"><path d="M15 2l12 6v12l-12 6-12-6V8z"/><path d="M3 8l12 6 12-6M15 14v12"/></svg></div>
  <div><h3>Production Process</h3><p>Duis aute irure dolor in reprehenderit in voluptate velit esse cillum dolore eu fugiat nulla pariatur. Excepteur sint occaecat cupidatat non proident, sunt in culpa qui officia deserunt mollit anim id est laborum.</p></div>
</div>

<div class="abs bg" style="top:3498px;width:1200px;height:914px;background:var(--grey)"></div>
<div class="abs gallery-main" role="img" aria-label="Photo: plush chihuahua toy with a purple bow"></div>
<div class="abs gallery-head"><h2>OUR GALLERY</h2><p>Duis aute irure dolor in reprehenderit in voluptate velit esse cillum dolore eu fugiat nulla pariatur.</p></div>
<div class="abs thumb" style="left:77px;width:313px;background:linear-gradient(90deg,#f0c6d4 0%,#f3dde4 45%,#efe2d4 70%,#f4f4f4 100%)" role="img" aria-label="Photo: pink plush handbag beside a plush chihuahua"></div>
<div class="abs thumb" style="left:419px;width:318px" role="img" aria-label="Photo: plush chihuahua toy, front view"></div>
<div class="abs thumb" style="left:766px;width:305px" role="img" aria-label="Photo: close-up of plush chihuahua face"></div>
<div class="abs thumb" style="left:1104px;width:96px" role="img" aria-label="Photo: plush chihuahua toy, side view"></div>

<div class="abs say-head"><h2>WHAT<br>PEOPLE SAY</h2><p>Duis aute irure dolor in reprehenderit in voluptate velit esse cillum dolore eu fugiat nulla pariatur.</p></div>
<div class="abs card" style="left:336px;width:442px">
  <div class="avatar" style="background:linear-gradient(160deg,#e8c89a,#c99478)" role="img" aria-label="Portrait photo of reviewer"></div>
  <p>Duis aute irure dolor in reprehenderit in voluptate velit esse cillum dolore eu fugiat nulla pariatur.</p>
  <h4>Manu</h4><small>Illinois</small><span class="quote">“</span>
</div>
<div class="abs card" style="left:814px;width:442px">
  <div class="avatar" style="background:linear-gradient(160deg,#6b4a3a,#3a2620)" role="img" aria-label="Portrait photo of reviewer"></div>
  <p>Duis aute irure dolor in reprehenderit in voluptate velit esse cillum dolore eu fugiat nulla pariatur.</p>
  <h4>Tobi</h4><small>Illinois</small><span class="quote">“</span>
</div>

<div class="abs scallop"></div>

<section class="abs contact">
  <div class="intro"><h2>Let’s Create<br>Progress Together</h2><p>Duis aute irure dolor in reprehenderit in voluptate velit esse cillum dolore eu fugiat nulla pariatur.</p></div>
  <form>
    <div class="field">Fullname</div>
    <div class="field">Phone Number</div>
    <div class="field">Your Email</div>
    <div class="field">Address</div>
    <div class="field">Message</div>
    <div class="btn send">Send</div>
  </form>
</section>

<div class="abs footer" style="left:270px;width:200px">
  <h4>Velvet Porter</h4>
  <div class="contact-line"><svg width="10" height="10" viewBox="0 0 10 10" fill="#fff"><path d="M5 0l5 5H8.5v5h-2.5V7H4v3H1.5V5H0z"/></svg><span>14 Harbor Lane, Linwood<br>OR 97000, United States</span></div>
  <div class="contact-line"><svg width="10" height="10" viewBox="0 0 10 10" fill="#fff"><path d="M2 0l2 2.5-1 1.3c.6 1.3 1.6 2.3 2.9 2.9l1.3-1L10 8l-1.5 2C4 10 0 6 0 1.5z"/></svg><span>(555) 210-4400</span></div>
  <div class="contact-line"><svg width="10" height="10" viewBox="0 0 10 10" fill="#fff"><path d="M2 0l2 2.5-1 1.3c.6 1.3 1.6 2.3 2.9 2.9l1.3-1L10 8l-1.5 2C4 10 0 6 0 1.5z"/></svg><span>(555) 210-4411</span></div>
</div>
<div class="abs footer footer-col" style="left:512px"><h4>Voluptate</h4><ul><li>Duis aute</li><li>Velit ess</li><li>Pariatur</li><li>Dolore eu</li></ul></div>
<div class="abs footer footer-col" style="left:674px"><h4>Voluptate</h4><ul><li>Duis aute</li><li>Velit ess</li><li>Pariatur</li><li>Dolore eu</li></ul></div>
<div class="abs footer footer-col" style="left:835px"><h4>Voluptate</h4><ul><li>Duis aute</li><li>Velit ess</li><li>Pariatur</li><li>Dolore eu</li></ul></div>
<p class="abs legal">2022 consectetur adipiscing elit, sed do eiusmod tempor incididunt ut labore</p>
<div class="abs social"><span></span><span></span><span></span></div>

</body>
</html>
```